Commercial Loan Originator Business Card (CHANGE COLORS SCHEME)

CHANGE COLOR SCHEME - SAME DESIGN

Name Marissa Lantham
Title Commercial Loan Originator
Office (800) 641-2905 x68
Direct (240) 617-2435
Email brightleaf4you@mailpost.example

Name Derek Fallow
Office (800) 641-2905 x70
Direct (410) 932-1864
Email d.falthebroker@mailpost.example

Name Gordon Wexley
Office (800) 641-2905 x71
Direct (215) 346-2081
Email g.wexley37@mailpost.example

Name Lyn Moreau
Office (800) 641-2905 x
Direct (202) 458-1937
Email lmoreau64@mailpost.example

Name Nadia Strand
Office (800) 641-2905 x72
Direct (240) 871-5246
Email qrzhomelending@mailpost.example

```html
<!DOCTYPE html>
<html lang="en">
<head>
<meta charset="utf-8">
<title>Commercial Loan Originator Business Cards</title>
<link href="https://fonts.googleapis.com/css2?family=Lato:wght@400;700&display=swap" rel="stylesheet">
<style>
  :root {
    --backdrop: #d3d5d8;
    --card-white: #ffffff;
    --band-raspberry: #a8325e;
    --band-forest: #1f3b33;
    --band-teal: #173d4f;
    --band-espresso: #43362d;
    --band-text: #ffffff;
    --contact-text: #263a46;
    --icon: #173d4f;
  }
  * { box-sizing: border-box; margin: 0; padding: 0; }
  html, body { width: 1200px; height: 1132px; overflow: hidden; }
  body {
    background: var(--backdrop);
    font-family: "Lato", "Helvetica Neue", Arial, sans-serif;
    position: relative;
  }
  .card {
    position: absolute;
    width: 470px;
    height: 268px;
    border-radius: 24px;
    background: var(--card-white);
    overflow: hidden;
    box-shadow: 0 3px 8px rgba(0,0,0,0.18);
  }
  .card--marissa { left: 64px;  top: 100px; --band: var(--band-raspberry); }
  .card--derek   { left: 599px; top: 116px; --band: var(--band-forest); }
  .card--gordon  { left: 74px;  top: 451px; --band: var(--band-teal); }
  .card--lyn     { left: 585px; top: 451px; --band: var(--band-teal); }
  .card--nadia   { left: 311px; top: 777px; --band: var(--band-espresso); }

  .card__band {
    position: absolute; left: 0; top: 0; width: 100%; height: 132px;
    background: var(--band);
  }
  .card__identity {
    position: absolute; left: 34px; top: 62px; color: var(--band-text); z-index: 2;
  }
  .card__name {
    font-weight: 700; font-size: 22px; line-height: 1; letter-spacing: -0.2px;
    text-transform: uppercase;
  }
  .card__title { font-weight: 400; font-size: 13px; margin-top: 6px; }

  .card__contacts {
    position: absolute; left: 34px; top: 160px; list-style: none; z-index: 2;
    color: var(--contact-text); font-size: 13px;
  }
  .card__contacts li { display: flex; align-items: center; height: 19.5px; white-space: nowrap; }
  .card__contacts svg { width: 13px; height: 13px; margin-right: 7px; fill: var(--icon); flex: none; }

  .card__portrait { position: absolute; bottom: 0; z-index: 1; }
  .card--marissa .card__portrait { left: 300px; width: 170px; height: 244px;
    border-radius: 70px 0 0 0;
    background: linear-gradient(180deg, #6e4538 0 32%, #c64a82 50%, #d9609a 100%); }
  .card--derek .card__portrait { left: 290px; width: 146px; height: 263px;
    border-radius: 50px 50px 0 0;
    background: linear-gradient(180deg, #3a2a22 0 16%, #3f4a44 26%, #2f3832 100%); }
  .card--gordon .card__portrait { left: 300px; width: 170px; height: 264px;
    border-radius: 60px 0 0 0;
    background: linear-gradient(180deg, #3b281f 0 32%, #22365a 48%, #1d2c48 100%); }
  .card--lyn .card__portrait { left: 300px; width: 160px; height: 258px;
    border-radius: 70px 70px 0 0;
    background: linear-gradient(180deg, #5b4a44 0 14%, #7a4e3a 24%, #7a4e3a 52%, #6c5370 70%, #8a5a8a 100%); }
  .card--nadia .card__portrait { left: 300px; width: 170px; height: 261px;
    border-radius: 70px 0 0 0;
    background: linear-gradient(180deg, #7a2a2a 0 12%, #6a4636 26%, #241f1e 46%, #1e1b1a 100%); }
</style>
</head>
<body>
<svg width="0" height="0" style="position:absolute" aria-hidden="true">
  <defs>
    <symbol id="icon-desk-phone" viewBox="0 0 16 16">
      <path d="M1 5.5C1 3.5 4 2.5 8 2.5s7 1 7 3v1.5h-3.5V5.5c-1-.4-2.2-.6-3.5-.6s-2.5.2-3.5.6V7H1z"/>
      <path d="M4.5 7.5h7l2 5.5v1.5h-11V13z"/>
      <rect x="6" y="9" width="4" height="3.5" fill="#fff"/>
    </symbol>
    <symbol id="icon-mobile" viewBox="0 0 16 16">
      <path d="M3.2 1.5l2.3 2.6-1.3 1.7c.9 2 2.4 3.6 4.4 4.6l1.7-1.3 2.6 2.3-1.6 2.6C6.3 13.4 2.4 9.6.8 4.6z"/>
      <path d="M9 1.2a6 6 0 0 1 5.8 5.8h-1.3A4.7 4.7 0 0 0 9 2.5zM9 3.8a3.4 3.4 0 0 1 3.2 3.2h-1.3A2.1 2.1 0 0 0 9 5.1z"/>
    </symbol>
    <symbol id="icon-mail" viewBox="0 0 16 16">
      <path d="M1 3h14v1.2L8 9 1 4.2z"/>
      <path d="M1 5.6l7 4.8 7-4.8V13H1z"/>
    </symbol>
  </defs>
</svg>

<article class="card card--marissa">
  <div class="card__band"></div>
  <div class="card__portrait" role="img" aria-label="Portrait photo of Marissa Lantham in a pink blouse"></div>
  <header class="card__identity">
    <h2 class="card__name">Marissa Lantham</h2>
    <p class="card__title">Commercial Loan Originator</p>
  </header>
  <ul class="card__contacts">
    <li><svg><use href="#icon-desk-phone"/></svg>(800) 641-2905 x68</li>
    <li><svg><use href="#icon-mobile"/></svg>(240) 617-2435</li>
    <li><svg><use href="#icon-mail"/></svg>brightleaf4you@mailpost.example</li>
  </ul>
</article>

<article class="card card--derek">
  <div class="card__band"></div>
  <div class="card__portrait" role="img" aria-label="Full-length photo of Derek Fallow in a dark plaid suit"></div>
  <header class="card__identity">
    <h2 class="card__name">Derek Fallow</h2>
    <p class="card__title">Commercial Loan Originator</p>
  </header>
  <ul class="card__contacts">
    <li><svg><use href="#icon-desk-phone"/></svg>(800) 641-2905 x70</li>
    <li><svg><use href="#icon-mobile"/></svg>(410) 932-1864</li>
    <li><svg><use href="#icon-mail"/></svg>d.falthebroker@mailpost.example</li>
  </ul>
</article>

<article class="card card--gordon">
  <div class="card__band"></div>
  <div class="card__portrait" role="img" aria-label="Portrait photo of Gordon Wexley in a navy suit and tie"></div>
  <header class="card__identity">
    <h2 class="card__name">Gordon Wexley</h2>
    <p class="card__title">Commercial Loan Originator</p>
  </header>
  <ul class="card__contacts">
    <li><svg><use href="#icon-desk-phone"/></svg>(800) 641-2905 x71</li>
    <li><svg><use href="#icon-mobile"/></svg>(215) 346-2081</li>
    <li><svg><use href="#icon-mail"/></svg>g.wexley37@mailpost.example</li>
  </ul>
</article>

<article class="card card--lyn">
  <div class="card__band"></div>
  <div class="card__portrait" role="img" aria-label="Portrait photo of Lyn Moreau in glasses and a patterned top"></div>
  <header class="card__identity">
    <h2 class="card__name">Lyn Moreau</h2>
    <p class="card__title">Commercial Loan Originator</p>
  </header>
  <ul class="card__contacts">
    <li><svg><use href="#icon-desk-phone"/></svg>(800) 641-2905 x</li>
    <li><svg><use href="#icon-mobile"/></svg>(202) 458-1937</li>
    <li><svg><use href="#icon-mail"/></svg>lmoreau64@mailpost.example</li>
  </ul>
</article>

<article class="card card--nadia">
  <div class="card__band"></div>
  <div class="card__portrait" role="img" aria-label="Seated portrait photo of Nadia Strand in a black top"></div>
  <header class="card__identity">
    <h2 class="card__name">Nadia Strand</h2>
    <p class="card__title">Commercial Loan Originator</p>
  </header>
  <ul class="card__contacts">
    <li><svg><use href="#icon-desk-phone"/></svg>(800) 641-2905 x72</li>
    <li><svg><use href="#icon-mobile"/></svg>(240) 871-5246</li>
    <li><svg><use href="#icon-mail"/></svg>qrzhomelending@mailpost.example</li>
  </ul>
</article>
</body>
</html>
```